Business Card Design Coralgate Airflow Solutions

The Business will be centred around supply and installation of Ventilation for domestic homes and warehousing/workshops, and will be marketed as a Eco friendly means of reducing your carbon footprint and reducing energy consumption.Our suppliers will provide a range of products that will ventilate roof spaces and later will branch into to air transfer within homes for cooling and heating other rooms of the home etc.I would like to see colours that would be commensurate with the logo provided and yet not dominate the logo.Final design should convey a Diverse , professional but friendly service that will suit client needs

Target Market(s)

Domestic home owners and warehousing/workshop businesses

Industry/Entity Type

Business

Contact Information for Business Card

Company Name: Coralgate Airflow Solutions Pty Ltd, ABN: 42 817 359 264, Address: 27 Marrowfen Tulvanna W.A 6289, Email: dale@coralgateairflowsolutions.com.au, Mobile Number: 0461 852 309

Requirements
Nice to have
• A tract art that commensurate of the logo supplied
Should not have
• Font style that opposes logo design

```html
<!DOCTYPE html>
<html lang="en">
<head>
<meta charset="utf-8">
<title>Coralgate Airflow Solutions – Business Card</title>
<link rel="stylesheet" href="https://fonts.googleapis.com/css2?family=Lato:wght@400;700&display=swap">
<style>
  :root {
    --green: #20b24a;
    --brown: #5a2527;
    --red: #e0383c;
    --charcoal: #2e2c2d;
    --white: #ffffff;
    --muted: #9a9a9a;
    --backdrop: #e9e6e1;
  }
  * { box-sizing: border-box; margin: 0; padding: 0; }
  html, body { width: 1200px; height: 871px; overflow: hidden; }
  body {
    background: var(--backdrop);
    font-family: "Lato", Arial, sans-serif;
    position: relative;
  }
  .card {
    position: absolute;
    left: 320px;
    width: 560px;
    height: 320px;
    overflow: hidden;
    box-shadow: 0 6px 18px rgba(0,0,0,0.18);
  }
  .card--front { top: 70px; background: var(--white); }
  .card--back { top: 480px; background: var(--charcoal); }

  .band { position: absolute; }
  .band--green { background: var(--green); }
  .band--brown { background: var(--brown); }

  /* front */
  .front-brand {
    position: absolute; left: 120px; top: 92px;
    display: flex; align-items: center; gap: 12px;
  }
  .brand-mark { width: 20px; height: 20px; background: var(--green); }
  .brand-name {
    font-weight: 700; font-size: 30px; color: var(--brown); line-height: 1.1;
  }
  .front-rule {
    position: absolute; left: 14px; right: 14px; top: 196px; height: 4px;
    background: var(--green);
  }
  .abn-ribbon {
    position: absolute; left: 110px; top: 178px; width: 250px; height: 40px;
  }
  .abn-text {
    position: absolute; left: 110px; top: 178px; width: 250px; height: 40px;
    display: flex; align-items: center; justify-content: center;
    color: var(--white); font-size: 16px; letter-spacing: 0.3px;
  }
  .front-tagline {
    position: absolute; left: 120px; top: 132px;
    font-size: 16px; color: var(--green); letter-spacing: 1px;
  }

  /* back */
  .back-panel {
    position: absolute; left: 0; top: 0; width: 262px; height: 320px;
    background: var(--white);
  }
  .back-brand {
    position: absolute; left: 30px; top: 146px; width: 210px;
    display: flex; align-items: center; gap: 8px;
  }
  .back-brand .brand-mark { width: 12px; height: 12px; flex: none; }
  .back-brand .brand-name { font-size: 17px; }

  .back-info { position: absolute; left: 290px; top: 30px; right: 20px; color: var(--white); }
  .company { display: flex; gap: 14px; align-items: flex-start; }
  .company-bars { display: flex; gap: 5px; margin-top: 8px; }
  .company-bars span { width: 5px; height: 24px; background: var(--green); }
  .company-name { font-weight: 700; font-size: 15px; }
  .company-sub { font-size: 10px; color: var(--muted); margin-top: 2px; }

  .contact-list { list-style: none; margin-top: 22px; }
  .contact-item { display: flex; align-items: center; gap: 14px; margin-bottom: 14px; }
  .contact-icon {
    width: 26px; height: 26px; flex: none;
    display: flex; align-items: center; justify-content: center;
    background: var(--green);
  }
  .contact-icon--mail { background: var(--red); }
  .contact-text { font-size: 13px; line-height: 1.35; }
  .contact-text--small { font-size: 10px; }
</style>
</head>
<body>

<section class="card card--front" aria-label="Business card front">
  <!-- frame bands -->
  <div class="band band--green" style="left:0;top:0;width:140px;height:14px"></div>
  <div class="band band--brown" style="left:0;top:14px;width:14px;height:90px"></div>
  <div class="band band--green" style="left:0;top:104px;width:14px;height:216px"></div>
  <div class="band band--green" style="left:0;top:306px;width:90px;height:14px"></div>
  <div class="band band--green" style="left:420px;top:306px;width:140px;height:14px"></div>
  <div class="band band--green" style="left:546px;top:0;width:14px;height:200px"></div>
  <div class="band band--brown" style="left:546px;top:200px;width:14px;height:120px"></div>

  <div class="front-brand">
    <span class="brand-mark"></span>
    <span class="brand-name">Coralgate Airflow Solutions</span>
  </div>

  <div class="front-rule"></div>
  <svg class="abn-ribbon" viewBox="0 0 250 40" aria-hidden="true">
    <polygon points="0,0 250,0 250,40 0,40" fill="#20b24a"/>
    <polygon points="0,40 -0,40 12,50 12,40" fill="#5a2527"/>
  </svg>
  <div class="abn-text">ABN: 42 817 359 264</div>
</section>

<section class="card card--back" aria-label="Business card back">
  <div class="back-panel"></div>
  <div class="band band--green" style="left:0;top:0;width:14px;height:110px"></div>
  <div class="band band--brown" style="left:0;top:110px;width:14px;height:110px"></div>
  <div class="band band--green" style="left:0;top:220px;width:14px;height:100px"></div>
  <div class="band band--green" style="left:0;top:306px;width:120px;height:14px"></div>
  <div class="band band--brown" style="left:120px;top:306px;width:90px;height:14px"></div>
  <div class="band band--green" style="left:210px;top:306px;width:52px;height:14px"></div>
  <div class="band band--green" style="left:248px;top:0;width:14px;height:70px"></div>
  <div class="band band--brown" style="left:248px;top:70px;width:14px;height:170px"></div>
  <div class="band band--green" style="left:248px;top:240px;width:14px;height:80px"></div>

  <div class="back-brand">
    <span class="brand-mark"></span>
    <span class="brand-name">Coralgate Airflow Solutions</span>
  </div>

  <div class="back-info">
    <div class="company">
      <div class="company-bars"><span></span><span></span></div>
      <div>
        <div class="company-name">Coralgate Airflow Solutions</div>
        <div class="company-sub">Pty Ltd</div>
      </div>
    </div>

    <ul class="contact-list">
      <li class="contact-item">
        <span class="contact-icon">
          <svg width="12" height="14" viewBox="0 0 12 14" aria-hidden="true"><rect x="1.5" y="0.5" width="9" height="13" rx="1.5" fill="none" stroke="#fff"/><circle cx="6" cy="11" r="0.9" fill="#fff"/></svg>
        </span>
        <span class="contact-text">0461 852 309</span>
      </li>
      <li class="contact-item">
        <span class="contact-icon contact-icon--mail">
          <svg width="14" height="10" viewBox="0 0 14 10" aria-hidden="true"><rect x="0.5" y="0.5" width="13" height="9" fill="none" stroke="#fff"/><polyline points="0.5,0.5 7,6 13.5,0.5" fill="none" stroke="#fff"/></svg>
        </span>
        <span class="contact-text contact-text--small">dale@coralgateairflowsolutions<br>.com.au</span>
      </li>
      <li class="contact-item">
        <span class="contact-icon">
          <svg width="10" height="14" viewBox="0 0 10 14" aria-hidden="true"><path d="M5 0.5a4.5 4.5 0 0 1 4.5 4.5c0 3.3-4.5 8.5-4.5 8.5S0.5 8.3 0.5 5A4.5 4.5 0 0 1 5 0.5z" fill="#fff"/><circle cx="5" cy="5" r="1.6" fill="#20b24a"/></svg>
        </span>
        <span class="contact-text">27 Marrowfen Tulvanna<br>W.A 6289</span>
      </li>
    </ul>
  </div>
</section>

</body>
</html>
```